" O nome Valtessora significa dentro do movimento. A clínica tem como carro chefe um trabalho chamado de videoanálise de movimento. Usamos um software para realizar análise de marcha, corrida, salto, estabilidade, flexibilidade entre outros. Identificamos alteraçoes no movimento que possam ser a causa de dor ou diminmuiçao no rendimento físico-funcional. Alteraçoes identificadas entramos com a reabilitaçao usando Pilates, RPG, Hidroterapia, Treinamento Funcional, Osteopatia entre outros. Nosso foco: resultados! "

```html
<!DOCTYPE html>
<html lang="pt-BR">
<head>
<meta charset="utf-8">
<title>Valtessora – Papelaria</title>
<link rel="stylesheet" href="https://fonts.googleapis.com/css2?family=Exo+2:wght@400;700&display=swap">
<style>
  :root {
    --bg: #eef0f3;
    --paper-top: #ffffff;
    --paper-bottom: #c9d7ef;
    --brand: #1f318f;
    --brand-soft: #4f6fc0;
    --flap: #5d82c6;
    --flap-edge: #4a6fb6;
    --text-small: #2a3a8a;
  }
  * { margin: 0; padding: 0; box-sizing: border-box; }
  html, body {
    width: 1200px; height: 1200px; overflow: hidden;
    background: var(--bg);
    font-family: "Exo 2", sans-serif;
  }
  .stationery { position: relative; width: 1200px; height: 1200px; }
  .letterhead {
    position: absolute; left: 110px; top: 190px;
    width: 560px; height: 792px; overflow: hidden;
    background: linear-gradient(160deg, var(--paper-top) 0%, #eef3fb 40%, var(--paper-bottom) 100%);
  }
  .brand {
    position: absolute; left: 0; right: 0; z-index: 1;
    display: flex; flex-direction: column; align-items: center;
  }
  .letterhead .brand { top: 62px; }
  .brand-dot {
    width: 34px; height: 34px; border-radius: 50%;
    background: var(--brand); margin-bottom: 10px;
  }
  .brand-name {
    font-weight: 700; color: var(--brand);
    font-size: 46px; letter-spacing: -1px; line-height: 1;
  }
  .brand-tagline {
    margin-top: 6px; font-size: 11px; letter-spacing: 2.4px;
    color: var(--brand-soft);
  }
  .motif {
    position: absolute; left: -140px; top: 240px;
    width: 680px; height: 400px;
    background: radial-gradient(closest-side, rgba(42,63,158,0.5) 0%, rgba(90,115,195,0.35) 40%, rgba(159,182,227,0.15) 75%, rgba(159,182,227,0) 100%);
  }
  .envelope {
    position: absolute; left: 720px; top: 290px;
    width: 380px; height: 538px;
    background: linear-gradient(165deg, #ffffff 0%, #e7eef9 50%, var(--paper-bottom) 100%);
    overflow: hidden;
  }
  .envelope-flap { position: absolute; left: 0; top: 0; width: 380px; height: 80px; }
  .envelope .brand { bottom: 112px; }
  .envelope .brand-dot { width: 26px; height: 26px; margin-bottom: 8px; }
  .envelope .brand-name { font-size: 34px; }
  .envelope .brand-tagline { font-size: 9px; letter-spacing: 1.8px; }
  .contact {
    position: absolute; left: 0; right: 0; bottom: 34px;
    text-align: center; color: var(--text-small);
    font-size: 10px; line-height: 1.6;
  }
  .contact .web { margin-top: 6px; font-size: 13px; letter-spacing: 5px; }
</style>
</head>
<body>
<main class="stationery">
  <section class="letterhead">
    <div class="brand">
      <span class="brand-dot"></span>
      <span class="brand-name">Valtessora</span>
      <span class="brand-tagline">Clínica de Performance Humana</span>
    </div>
    <div class="motif" role="img" aria-label="Área do grande motivo decorativo da marca em tons de azul"></div>
  </section>

  <section class="envelope">
    <svg class="envelope-flap" viewBox="0 0 380 80" aria-hidden="true">
      <path d="M0 0 H380 V80 L350 60 H0 Z" fill="var(--flap)"/>
      <path d="M0 60 H350 L380 80" fill="none" stroke="var(--flap-edge)" stroke-width="1"/>
    </svg>
    <div class="brand">
      <span class="brand-dot"></span>
      <span class="brand-name">Valtessora</span>
      <span class="brand-tagline">Clínica de Performance Humana</span>
    </div>
    <div class="contact">
      <p>Rua das Acácias, 120 · Cep: 12345-000 · Porto Serrano - PS</p>
      <p>Tel (00) 0000-0000 · contato@valtessora.com.br</p>
      <p class="web">www.valtessora.com.br</p>
    </div>
  </section>
</main>
</body>
</html>
```